verdant manor grounds simple classy business card design

my name is owen brackley and I run a gardening business aimed at high class verdant manor grounds. the business name is verdant manor grounds and our logo was designed on brief hive .My clientel are anything from residential homes to businesses. I take pride in my work and know that I offer a service like no other in my area.
The business card will be used to represent my business and I want it to be not only rememberable, but simplistic and modern. Eye catching too. Of course I would like it relatable to gardening and appealing to the correct clientel - those being garden enthusiasts, prestigious homes and businesses that are after top of the line gardening services like no other on the market.
I am not a typical lawn mowing business so I don't want a typical card design that represents that. The gardens I work with are generally million dollar properties with owners who are very garden proud looking for upkeep and guidance from me along with sometimes whole new garden designs. I want the business cards to show to my clients that I take pride, as they do, in their garden. And I want them to know from my card that I am a professional, qualified horticulturist offering them a top of the line service for life. I want them to refer my business on. I want them to look at my business card and see class and professionalism in a modern unique bold way.
The card should be simple with the possibility of the logo on the front being embossed/debossed and my details on the back the card should have a organic garden feel it's very important to me that it is absolutely perfect
I am also very open to ideas and suggestions so look forward to seeing the designs. the business logo has been supplied with this project and I want the card to be double sided

Contact info is
Owen Brackley - Managing Director / Horticulturist
Phone : 0481 562 907
Email: owenbrackley@verdantmanorgrounds.example.au

Target Market(s)

high class gardens residential and commercial

Industry/Entity Type

Gardener

Contact Information for Business Card

Contact info is
Phone : 0481 562 907

PLEASE MAKE CARD DOUBLE SIDED

Requirements
Must have
• organic simple classy modern feel
• must flow with the current logo that has been supplied with this project
• Double sided
• Must explain in a simple way that I deal with high end gardens and I'm a qualified horticulturist
Nice to have
• embossed debossed logo
Should not have
• shouldn't be to busy or cheap looking

```html
<!DOCTYPE html>
<html lang="en">
<head>
<meta charset="utf-8">
<title>Verdant Manor Grounds – Business Card</title>
<link rel="stylesheet" href="https://fonts.googleapis.com/css2?family=Lora:wght@600;700&family=Montserrat:wght@500&family=Open+Sans:wght@400&display=swap">
<style>
  :root {
    --backdrop: #e9e5df;
    --charcoal: #3b3a37;
    --card-white: #f7f7f5;
    --leaf: #47a147;
    --leaf-soft: #5fb45a;
    --ink: #2b2b2b;
    --grey-text: #6a6a6a;
    --rule: #3a3a3a;
  }
  * { box-sizing: border-box; margin: 0; padding: 0; }
  html, body {
    width: 1200px; height: 801px; overflow: hidden;
    background: var(--backdrop);
  }
  .sheet {
    position: relative; width: 1200px; height: 801px;
    display: flex; align-items: center; justify-content: center; gap: 40px;
  }
  .card {
    width: 540px; height: 310px; position: relative;
    box-shadow: 0 6px 18px rgba(0,0,0,.15);
  }
  /* Front */
  .card--front {
    background: var(--charcoal);
    display: flex; align-items: center; justify-content: center;
  }
  .brand {
    display: flex; align-items: center; gap: 14px;
    font-family: "Lora", Georgia, serif; font-weight: 700;
    color: var(--leaf-soft); letter-spacing: 2px; text-transform: uppercase;
    line-height: 1.15;
  }
  .brand__dot {
    flex: none; border-radius: 50%; background: var(--leaf-soft);
  }
  .card--front .brand { font-size: 26px; }
  .card--front .brand__dot { width: 54px; height: 54px; }
  /* Back */
  .card--back {
    background: var(--card-white);
    display: flex; align-items: center;
    padding: 0 22px 0 26px;
  }
  .card--back .brand {
    width: 188px; font-size: 17px; color: var(--leaf); gap: 10px;
  }
  .card--back .brand__dot { width: 34px; height: 34px; background: var(--leaf); }
  .divider {
    width: 1.5px; height: 170px; background: var(--rule);
    margin: 0 20px 0 14px; flex: none;
  }
  .details { display: flex; flex-direction: column; }
  .details__name {
    font-family: "Montserrat", Arial, sans-serif; font-weight: 500;
    font-size: 21px; color: var(--ink);
  }
  .details__role {
    font-family: "Lora", Georgia, serif; font-weight: 700;
    font-size: 14px; color: var(--leaf); margin: 3px 0 14px;
  }
  .contact {
    display: flex; align-items: center; gap: 9px;
    font-family: "Open Sans", Arial, sans-serif; font-size: 12px;
    color: var(--grey-text); margin-bottom: 7px; white-space: nowrap;
  }
  .contact svg { width: 14px; height: 12px; flex: none; fill: var(--leaf); }
</style>
</head>
<body>
<main class="sheet">
  <section class="card card--front" aria-label="Card front">
    <div class="brand"><span class="brand__dot"></span><span>Verdant Manor<br>Grounds</span></div>
  </section>

  <section class="card card--back" aria-label="Card back">
    <div class="brand"><span class="brand__dot"></span><span>Verdant Manor<br>Grounds</span></div>
    <div class="divider"></div>
    <div class="details">
      <p class="details__name">Owen Brackley</p>
      <p class="details__role">Managing Director / Horticulturist</p>
      <p class="contact">
        <svg viewBox="0 0 14 12" aria-hidden="true"><path d="M1 3.5C3 1 11 1 13 3.5L12 5.2 9.6 4.4V3.3C8 2.8 6 2.8 4.4 3.3V4.4L2 5.2Z"/><rect x="3" y="6" width="8" height="5" rx="1"/></svg>
        0481 562 907
      </p>
      <p class="contact">
        <svg viewBox="0 0 14 12" aria-hidden="true"><path d="M1 2h12v8H1z M1.5 2.5 7 7l5.5-4.5" fill="none" stroke="var(--leaf)" stroke-width="1.4"/></svg>
        owenbrackley@verdantmanorgrounds.example.au
      </p>
    </div>
  </section>
</main>
</body>
</html>
```